"Breathe & Bloom" Book Cover 5.5x8.5

Title of the book is "Breathe & Bloom"
Subtitle is "Unmasking Pricing Myths"
I've used PixelGuild on multiple occasions you can look on my Borvex page, Mark Delwitt, to see the covers I've used in the other projects I've done.
The target audience are people who have been tricked to think they can't retire because inflation, i.e. cost of living is going up so much they must work to keep up. There is no evidence of this.
And those are the people I want to reach so they can "Breathe...and Bloom."
Target Market(s)
Americans aged 55 and over who are thinking about retirement
Industry/Entity Type
Financial
Requirements
Nice to have
- Keep It Simple, Stupid is my mantra. Just make it pop out when people are browsing
Should not have
- No piggy banks. No old people sitting on a beach.

```html
<!DOCTYPE html>
<html lang="en">
<head>
<meta charset="utf-8">
<title>Breathe &amp; Bloom — Book Cover</title>
<link rel="stylesheet" href="https://fonts.googleapis.com/css2?family=Catamaran:wght@300;600&family=Open+Sans:wght@600&display=swap">
<style>
  :root {
    --sky-top: #6cc5fd;
    --sky-mid: #b8e3fd;
    --haze: #ffffff;
    --water-top: #cdeefc;
    --water-bottom: #d9f3fd;
    --title-navy: #0d1463;
    --amp-white: #ffffff;
    --subtitle-blue: #2b4c86;
    --author-blue: #1d5c9e;
    --boat-white: #f4f8fc;
    --boat-pale: #b9d2ee;
    --boat-blue: #5f93d6;
    --boat-deep: #2559b4;
  }
  * { margin: 0; padding: 0; box-sizing: border-box; }
  html, body { width: 750px; height: 1200px; overflow: hidden; }
  .cover {
    position: relative;
    width: 750px;
    height: 1200px;
    overflow: hidden;
    background: linear-gradient(to bottom,
      var(--sky-top) 0%,
      var(--sky-mid) 30%,
      var(--haze) 56%,
      var(--haze) 68.5%,
      var(--water-top) 69%,
      var(--water-bottom) 100%);
  }
  .title {
    position: absolute;
    inset: 0;
    font-family: "Catamaran", sans-serif;
    font-weight: 600;
    color: var(--title-navy);
    line-height: 1;
  }
  .title-first {
    position: absolute;
    left: 48px;
    top: 76px;
    font-size: 136px;
    letter-spacing: -3px;
  }
  .title-amp {
    position: absolute;
    left: 486px;
    top: 62px;
    font-weight: 300;
    font-size: 236px;
    color: var(--amp-white);
  }
  .title-second {
    position: absolute;
    right: 76px;
    top: 252px;
    font-size: 136px;
    letter-spacing: -3px;
  }
  .subtitle {
    position: absolute;
    left: 0;
    right: 0;
    top: 426px;
    text-align: center;
    font-family: "Catamaran", sans-serif;
    font-weight: 600;
    font-size: 51px;
    letter-spacing: -0.5px;
    color: var(--subtitle-blue);
  }
  .boat-photo {
    position: absolute;
    left: 130px;
    top: 606px;
    width: 460px;
    height: 368px;
  }
  .author {
    position: absolute;
    left: 0;
    right: 0;
    top: 1052px;
    text-align: center;
    font-family: "Open Sans", sans-serif;
    font-weight: 600;
    font-size: 50px;
    letter-spacing: 0.15em;
    padding-left: 0.15em;
    color: var(--author-blue);
  }
</style>
</head>
<body>
  <main class="cover">
    <h1 class="title">
      <span class="title-first">Breathe</span>
      <span class="title-amp">&amp;</span>
      <span class="title-second">Bloom</span>
    </h1>
    <p class="subtitle">UNMASKING PRICING MYTHS</p>
    <svg class="boat-photo" viewBox="0 0 460 368" role="img" aria-label="Photograph of a white and blue folded paper boat floating on calm water, its deep blue reflection showing below the waterline">
      <defs>
        <linearGradient id="boatTone" x1="0" y1="0" x2="0" y2="1">
          <stop offset="0" stop-color="var(--boat-white)"/>
          <stop offset="0.45" stop-color="var(--boat-pale)"/>
          <stop offset="0.6" stop-color="var(--boat-blue)"/>
          <stop offset="0.63" stop-color="var(--boat-deep)"/>
          <stop offset="0.85" stop-color="var(--boat-deep)"/>
          <stop offset="1" stop-color="var(--boat-blue)"/>
        </linearGradient>
      </defs>
      <rect x="0" y="0" width="460" height="368" rx="24" fill="url(#boatTone)"/>
    </svg>
    <p class="author">MARK DELWITT</p>
  </main>
</body>
</html>
```